Brennick Setter Club - Rare dog breed club needs web design!

The Transylvanian Hound (or Erdélyi kopó) is an ancient Hungarian dog breed. These medium-sized hounds were favored by the Hungarian kings and princes for hunting bears and wolves in the Carpathian mountains of Transylvania. The breed's great adaptability to the region's extreme climates of sweltering summers and frigid winters made it an excellent all season hunting dog. This dog has a sleek appearance and stunning good looks. They are lean, appear very elegant and proud. Their erect posture and beautifully sculpted head portray great attentiveness and authority. In general, this rare breed is extremely good natured, loyal and obedient. It has a tendency to form strong attachments to its primary caretakers and will remain loyal and protective. (Please refer to existing web resources.)

The Brennick Setter Club - with current website www.brennicksetter.com - is the official breed club of Transylvanian Hound afficionados, breeders and owners in the United States, which was founded in 2010. We are looking for a web design for the new, upgraded version of this central (currenty non-functioning) website. Please do not recycle the old logo (we may choose from your suggesions and pay for it!) or any of the old texts. Please use the structure described below. Overall, the webpage serves a dual purpose: an educational one (about the breed itself) and a community-building one (inside the Club). The proposed structure of the website is as follows:

1. About the Kopó
- Breed History
- Breed Standard
- Public Education
- Photo Gallery

2. Life with a Kopó
- Health and Genetics
- Feeding and Nutrition
- Training and Activities

3. Finding a Kopó
- Is this the Right Breed for You?
- Choosing a Puppy
- FAQ
- Breeder Referral

4. The Brennick Setter Club
- Constituton
- Officers and Appointees
- Code of Ethics
- Breeder Guidelines
- Membership
- Reports
- Links

5. News and Events

6. Shop

We are attaching a couple of examples of the graphics/drawings of the dogs that would be part of the design of the website. We plan to have more of these artistic depictions, nicely embedded into the background (maybe shaded out at the edges just like the drawings themselves) and less actual photos. Or a good combination of the two.

Further information upon request.

Reason: There are a few very promising design collaborations ongoing. As we moved the brief to a more artistic and graphic direction, we felt that one week of extension would be needed to get to the perfect end-product, which could include designs for sub-pages as well.

Reason: In order to make the final modifications to the leading designs, and at the request of those designers, the deadline is extended until Friday.

Target Market(s)

- BRSC Club members, dog (especially T-Hound) owners, past and future owners, breeders, puppy buyers, hunters, kennel clubs, dog show participants, vets, animal shelters, Hungarian, Romanian and other European web visitors, historians

Industry/Entity Type

Club

Font styles to use
Serif
Decorative
Script

Requirements
Must have
• - Sync with graphics of dogs (see attachments), but accentuate the rich black basic color of the dogs
- Elegance, aristocratic/noble look and feel (but not overly archaic)
- Love, companionship, dogs as family members
- Hunting usage, but no bloody associations, rather romantic ones
- Simple to use and navigate for non-web-natives
- Old world (Central European) atmosphere, even the exotic, rustic and romantic Transylvanian feel - SEE the new attachment for inspiration (this was a design plan which we discarded (mainly because of its gothic, (nazi-like), unreadable font, and the fact that the plan makes the black-looking dogs appear brown), however we loved the fact that it was not full of boxes/windows, had a marble/sand stone like continuous background, lots of little elegant graphics, the drawings embedded, etc.
Nice to have
• - Working on smartphone, Zentabs, etc., so dynamic website design
- Web shop to be added to functionalities in the future (?)
- English language for now, in the future can be Hungarian, Romanian, etc., so the font choice should handle various alphabets
- Focus on the dogs (likely more graphics than photos, at least on the main pages), and not on the activities/humans - the design should accentuate the black and not the tan of the graphics!
Should not have
• - Old logo from the old www.brennicksetter.com webpage or the other logo from the Chatterly site of the Brennick Setter Club, we will have a new one (maybe designed by you!)
- Breed club, kennel club cliches
- Cutesy, adorable, cheesy design elements
- Old, stale, monolithic, archaic, snobbish, etc. look and feel
- No vampire associations

```html
<!DOCTYPE html>
<html lang="en">
<head>
<meta charset="utf-8">
<title>Brennick Setter Club</title>
<link rel="stylesheet" href="https://fonts.googleapis.com/css2?family=Open+Sans:wght@400;600;700&display=swap">
<style>
:root{
  --ink:#1b1b1b;
  --ink-2:#111;
  --gold:#f1b51c;
  --gold-deep:#e0a210;
  --orange:#f39a16;
  --paper:#fff;
  --text:#333;
  --muted:#777;
  --rule:#e2e2e2;
  --footer-text:#ccc;
  --field:#3a3a3a;
  --head:'Open Sans',Arial,sans-serif;
  --body:Arial,Helvetica,sans-serif;
}
*{box-sizing:border-box;margin:0;padding:0}
html,body{width:952px;height:1200px;overflow:hidden}
body{position:relative;background:var(--ink);font-family:var(--body);color:var(--text)}
.gold-band{position:absolute;left:0;top:374px;width:952px;height:590px;
  background:linear-gradient(180deg,#e1a412 0%,#ecb629 50%,#f6e09a 100%)}
.abs{position:absolute}

/* header */
.brand{left:112px;top:12px;width:110px;height:110px;border-radius:50%;border:3px solid #fff;
  display:flex;align-items:center;justify-content:center;text-align:center;
  font:600 13px/1.25 var(--head);color:#fff;padding:12px}
.club-tab{left:564px;top:0;width:264px;height:30px;background:var(--gold);border-radius:0 0 4px 4px;
  font:600 15px/30px var(--head);color:#fff;text-align:center;letter-spacing:.3px}
.search{left:610px;top:69px;width:230px;height:24px;display:flex}
.search-field{flex:1;background:#fff;font:400 10px/24px var(--head);color:#555;padding-left:7px}
.search-btn{width:25px;background:var(--gold);display:flex;align-items:center;justify-content:center}

.main-nav{left:111px;top:137px;width:730px;height:32px;background:linear-gradient(#2a2a2a,#151515);
  border-bottom:3px solid var(--orange);display:flex;align-items:center;justify-content:space-between;padding:0 10px 0 3px}
.main-nav a{font:600 9.5px var(--head);color:#fff;text-decoration:none;padding:7px 11px;border-radius:3px}
.main-nav a.current{background:#242424;border:1px solid #3b3b3b}

/* panel */
.panel{left:111px;top:172px;width:730px;height:828px;background:var(--paper);border-radius:0 0 3px 3px}
.hero{left:0;top:0;width:730px;height:312px;overflow:hidden}
.hero-art{position:absolute;inset:0;background:linear-gradient(90deg,#d9d2c6 0%,#cfc6b8 55%,#bdb0a0 100%)}
.hero-dog{position:absolute;left:440px;top:20px;width:290px;height:270px;
  background:radial-gradient(ellipse at 55% 50%,#5a3a28 0%,#7b5a45 40%,rgba(189,176,160,0) 72%)}
.hero-copy{position:absolute;left:40px;top:76px;color:#5a5550}
.hero-copy h2{font:400 24px/1.4 var(--head)}
.hero-copy h2 span{display:block;font-size:28px}
.hero-copy p{font:400 10px/1.65 var(--head);color:#8a847c;margin-top:14px;width:300px}
.hero-curve{position:absolute;left:0;top:0}
.dots{position:absolute;left:335px;top:292px;display:flex;gap:4px}
.dots i{width:12px;height:12px;border-radius:50%;border:2px solid #8a847c;background:#fff}
.dots i.on{background:var(--orange)}

.section-title{font:600 13.5px var(--head);color:#111;text-transform:uppercase}
.view-all{left:658px;top:329px;width:57px;height:18px;background:var(--ink-2);border-radius:2px;
  font:600 8px/18px var(--head);color:var(--gold);text-align:center}
.rule{height:1px;background:var(--rule)}

.card{top:375px;width:164px;height:134px;border:1px solid #ddd;padding:2px;background:#fff}
.card-photo{position:relative;width:100%;height:100%;overflow:hidden}
.card-label{position:absolute;left:0;bottom:0;width:100%;height:33px;background:rgba(30,25,20,.78);
  display:flex;align-items:center;justify-content:space-between;padding:0 4px 0 6px;
  font:600 10px var(--head);color:#fff}
.card-go{width:31px;height:24px;background:#fff;border-radius:2px;color:#111;font:700 10px/24px var(--head);text-align:center;letter-spacing:1px}

.col{top:536px;width:224px}
.col-head{display:flex;justify-content:space-between;align-items:flex-end;height:22px;border-bottom:1px solid var(--rule);padding-bottom:4px}
.col-head h3{font:400 13.5px var(--head);color:#222;text-transform:uppercase}
.more{font:700 8px var(--head);color:#222;border-left:1px solid #ccc;padding-left:5px;display:flex;align-items:center;gap:5px}
.col p{font:400 8.4px/1.6 var(--body);text-align:justify;color:#333;margin-top:10px}
.col p + p{margin-top:14px}

.news-item{display:flex;gap:10px;padding:10px 0 11px;border-bottom:1px solid var(--rule)}
.news-date{flex:none;width:46px;height:46px;background:var(--gold-deep);color:#fff;text-align:center;
  font:600 13px/1.25 var(--head);padding-top:5px}
.news-item p{margin:0;font:400 8.4px/1.3 var(--body);text-align:justify}
.news-item a{display:block;margin-top:4px;font:700 8.4px var(--body);color:var(--orange);text-decoration:none;padding-left:3px}

/* footer */
.foot-col h4{font:700 8px var(--head);color:var(--gold);text-transform:uppercase;margin-bottom:11px}
.foot-col li{list-style:none;font:400 8.6px var(--body);color:var(--footer-text);height:18px}
.foot-col li.see{color:var(--gold);font-weight:700}
.signup{display:grid;grid-template-columns:95px 121px;row-gap:7px;font:400 8.6px var(--body);color:var(--footer-text)}
.signup div{height:16px;line-height:10px}
.signup .field{background:var(--field);border:1px solid #4a4a4a}
.social li{display:flex;align-items:center;gap:12px;height:25px}
.social i{width:19px;height:19px;border-radius:50%}
.foot-rule{left:0;top:1149px;width:952px;height:1px;background:#2e2e2e}
.copyright{left:0;top:1168px;width:952px;text-align:center;font:400 8.6px var(--body);color:var(--footer-text)}
</style>
</head>
<body>
<div class="gold-band"></div>

<header>
  <div class="abs brand">Brennick Setter Club</div>
  <div class="abs club-tab">BRENNICK SETTER CLUB</div>
  <div class="abs search">
    <div class="search-field">Search</div>
    <div class="search-btn"><svg width="12" height="12" viewBox="0 0 12 12"><circle cx="4.5" cy="4.5" r="3.2" fill="none" stroke="#fff" stroke-width="1.6"/><path d="M7 7l4 4" stroke="#fff" stroke-width="2"/></svg></div>
  </div>
  <nav class="abs main-nav">
    <a class="current">ABOUT THE KOPÓ</a><a>LIFE WITH A KOPÓ</a><a>FINDING A KOPÓ</a><a>THE BRENNICK SETTER CLUB</a><a>NEWS AND EVENTS</a><a>SHOP</a>
  </nav>
</header>

<main class="abs panel">
  <section class="abs hero">
    <div class="hero-art" role="img" aria-label="Textured sandstone background with a drawn portrait of a black and tan hound"></div>
    <div class="hero-dog" role="img" aria-label="Drawing of a hound's head looking left"></div>
    <div class="hero-copy">
      <h2>Mauris vel lacus vitae felis<span>Suspendisse Auam Molestie</span></h2>
      <p>Suspendisse quam leo molestie sed luctus quis feugiat in pede usce tellus Sed metus augue convallis et vehicula</p>
    </div>
    <svg class="hero-curve" width="730" height="312" viewBox="0 0 730 312">
      <path d="M0 282 Q365 342 730 282 L730 312 L0 312Z" fill="#fff"/>
      <path d="M0 282 Q365 342 730 282" fill="none" stroke="#f39a16" stroke-width="3"/>
    </svg>
    <div class="dots"><i class="on"></i><i></i><i></i><i></i></div>
  </section>

  <h2 class="abs section-title" style="left:15px;top:334px">Our Services</h2>
  <div class="abs view-all">VIEW ALL ▸</div>
  <div class="abs rule" style="left:15px;top:361px;width:700px"></div>

  <div class="abs card" style="left:15px"><div class="card-photo" role="img" aria-label="Golden retriever on grass" style="background:linear-gradient(#5e8a3a,#a9763e 60%,#7a5a32)"><div class="card-label">LOREM IPSUM DOLOR<span class="card-go">&gt;&gt;&gt;</span></div></div></div>
  <div class="abs card" style="left:195px"><div class="card-photo" role="img" aria-label="Golden puppy close-up" style="background:linear-gradient(#c9b79a,#b88a55 60%,#8a6a45)"><div class="card-label">LOREM IPSUM DOLOR<span class="card-go">&gt;&gt;&gt;</span></div></div></div>
  <div class="abs card" style="left:374px"><div class="card-photo" role="img" aria-label="Two golden retrievers resting" style="background:linear-gradient(#6a4a30,#c08a4a 55%,#8a6238)"><div class="card-label">LOREM IPSUM DOLOR<span class="card-go">&gt;&gt;&gt;</span></div></div></div>
  <div class="abs card" style="left:552px"><div class="card-photo" role="img" aria-label="Beagle puppy sitting in a meadow" style="background:linear-gradient(#4f7a34,#7ea050 55%,#5e6a40)"><div class="card-label">LOREM IPSUM DOLOR<span class="card-go">&gt;&gt;&gt;</span></div></div></div>
  <div class="abs rule" style="left:15px;top:517px;width:700px"></div>

  <section class="abs col" style="left:15px">
    <div class="col-head"><h3>Company Overview</h3><span class="more">MORE <svg width="6" height="8"><path d="M0 0L6 4L0 8Z" fill="#f39a16"/></svg></span></div>
    <p>Sed ut perspiciatis unde omnis iste natus error sit voluptatem accusantium doloremque laudantium, totam rem aperiam, eaque ipsa quae ab illo inventore veritatis et quasi architecto beatae vitae dicta sunt explicabo. Nemo enim ipsam voluptatem quia voluptas sit</p>
    <p>aspernatur aut odit aut fugit, sed quia consequuntur magni dolores eos qui ratione voluptatem sequi nesciunt. Neque porro quisquam est, qui dolorem ipsum quia dolor sit amet, consectetur, adipisci velit, sed quia non numquam eius modi tempora incidunt ut labore et dolore magnam aliquamaspernatur aut odit aut fugit, sed quia consequuntur magni dolores eos qui ratione voluptatem sequi nesciunt. Neque porro quisquam est, qui dolorem</p>
  </section>
  <section class="abs col" style="left:252px">
    <div class="col-head"><h3>Our Team</h3><span class="more">MORE <svg width="6" height="8"><path d="M0 0L6 4L0 8Z" fill="#f39a16"/></svg></span></div>
    <p>Sed ut perspiciatis unde omnis iste natus error sit voluptatem accusantium doloremque laudantium, totam rem aperiam, eaque ipsa quae ab illo inventore veritatis et quasi architecto beatae vitae dicta sunt explicabo. Nemo enim ipsam voluptatem quia voluptas sit</p>
    <p>aspernatur aut odit aut fugit, sed quia consequuntur magni dolores eos qui ratione voluptatem sequi nesciunt. Neque porro quisquam est, qui dolorem ipsum quia dolor sit amet, consectetur, adipisci velit, sed quia non numquam eius modi tempora incidunt ut labore et dolore magnam aliquamaspernatur aut odit aut fugit, sed quia consequuntur magni dolores eos qui ratione voluptatem sequi nesciunt. Neque porro quisquam est, qui dolorem</p>
  </section>
  <section class="abs col" style="left:491px">
    <div class="col-head"><h3>Latest News</h3><span class="more">MORE <svg width="6" height="8"><path d="M0 0L6 4L0 8Z" fill="#f39a16"/></svg></span></div>
    <div class="news-item"><div class="news-date">16<br>APR</div><div><p>ectetur adipisicing elit, sed do eiusmod tempor incididunt ut labore et dolore magna aliqua. Ut enim ad minim veniam,</p><a>Read More</a></div></div>
    <div class="news-item"><div class="news-date">16<br>APR</div><div><p>ectetur adipisicing elit, sed do eiusmod tempor incididunt ut labore et dolore magna aliqua. Ut enim ad minim veniam,</p><a>Read More</a></div></div>
    <div class="news-item" style="border-bottom:0"><div class="news-date">16<br>APR</div><div><p>ectetur adipisicing elit, sed do eiusmod tempor incididunt ut labore et dolore magna aliqua. Ut enim ad minim veniam,</p><a>Read More</a></div></div>
  </section>
</main>

<footer>
  <div class="abs foot-col" style="left:126px;top:1018px"><h4>Menu Links</h4><ul><li>Company overview</li><li>Heritage</li><li>Our Team</li><li>Partners</li><li>Privacy</li><li>Sitemap</li></ul></div>
  <div class="abs foot-col" style="left:237px;top:1018px"><h4>About Us</h4><ul><li>Events</li><li>Videos</li><li>Contacts</li><li>Utilities</li><li class="see">SEE MORE</li></ul></div>
  <div class="abs foot-col" style="left:343px;top:1018px"><h4>Support</h4><ul><li>Press releases</li><li>News stories</li><li>Media downloads</li><li>Awards</li><li>Events</li></ul></div>
  <div class="abs foot-col" style="left:466px;top:1018px"><h4>Hollis Wren Newsletter</h4>
    <div class="signup"><div>Name</div><div class="field"></div><div>Last Name</div><div class="field"></div><div>Email</div><div class="field"></div><div>I'm</div><div class="field"></div></div>
  </div>
  <div class="abs foot-col social" style="left:750px;top:1018px"><h4>Follow Us</h4><ul>
    <li><i style="background:#3b5998"></i>Chatterly</li>
    <li><i style="background:#d93a2b"></i>Vidora</li>
    <li><i style="background:#2aa3d8"></i>Chirply</li>
    <li><i style="background:#f08a24"></i>RSS</li>
  </ul></div>
  <div class="abs foot-rule"></div>
  <p class="abs copyright">© 2014 brennicksetter.com. All Rights Reserved.</p>
</footer>
</body>
</html>
```